Business Card and Stationary Design

After the successful redesign of our logo we are wanting to follow suite and create a new business card and stationary design!

New Logo is attached, information required on the business card should contain a mixture of the following but layout/arrangement is up to the designer.

Happy if the national provider number and abn are on the back, and happy for them to be smaller than the rest.

I am also happy to receive single sided or weird and wonderful designs.

Name
Title
National Provider Number 7291
ABN 53 219 864 317
Level 3, 42 Marlow Street
Kotara NSW 2289
Ph: 1300 987 214
Mobile: 0432 785 619
name@ferngatebuild.com.au
www.ferngatebuild.com.au

Target Market(s)

Professionals, Peers, Students, Suppliers...

Industry/Entity Type

Construction

Contact Information for Business Card

Listed in project description

Font styles to use
Other font styles liked:
• Century Gothic

Colors
0455a3
3176b5
ffffff

Requirements
Must have
• Professional Design, same color scheme as our logo
Nice to have
• Something that sets our apart from everyone else would be fantastic, open to size and shape and layout options, as long as they present professionally.
• Open to raised/embossed text, alternative materials, custom sizes, clear material
Should not have
• The color orange

```html
<!DOCTYPE html>
<html lang="en">
<head>
<meta charset="utf-8">
<title>Ferngate Build – Business Card</title>
<link rel="stylesheet" href="https://fonts.googleapis.com/css2?family=Lato:wght@400;700&family=Tinos&family=Questrial&display=swap">
<style>
  :root {
    --navy: #0b2a82;
    --royal: #1c3f93;
    --royal-light: #26489c;
    --ink: #1b1b1b;
    --grey: #7d7d7d;
    --paper: #ffffff;
    --canvas: #dcdde0;
    --pattern: #eef0f2;
  }
  * { margin: 0; padding: 0; box-sizing: border-box; }
  html, body { width: 1200px; height: 1200px; overflow: hidden; }
  body {
    background: var(--canvas);
    font-family: "Lato", Arial, sans-serif;
    position: relative;
  }
  .card {
    position: absolute;
    left: 150px;
    width: 900px;
    height: 500px;
    overflow: hidden;
  }
  /* Front */
  .card-front { top: 70px; background: var(--paper); }
  .front-pattern {
    position: absolute; left: 0; top: 0; width: 100%; height: 300px;
    background: linear-gradient(160deg, var(--pattern), #fafbfc 55%, var(--paper));
  }
  .front-band {
    position: absolute; left: 0; bottom: 0; width: 100%; height: 150px;
    background: var(--navy);
  }
  .wordmark {
    display: flex; align-items: center; gap: 12px;
    font-family: "Questrial", "Lato", sans-serif;
    white-space: nowrap; line-height: 1;
  }
  .wordmark-mark { display: block; width: 18px; height: 18px; flex: none; }
  .front-wordmark {
    position: absolute; right: 50px; top: 62px;
    font-size: 46px; color: var(--navy);
  }
  .front-wordmark .wordmark-mark { background: var(--navy); }
  .registration {
    position: absolute; right: 140px; top: 142px;
    font-size: 17px; color: var(--ink); white-space: nowrap;
  }
  .registration .sep {
    display: inline-block; width: 10px; height: 10px; background: var(--navy);
    margin: 0 10px 1px;
  }
  .identity {
    position: absolute; left: 320px; top: 180px; width: 400px; height: 110px;
    border: 2px solid var(--navy); background: var(--paper);
    padding: 8px 22px;
  }
  .identity-name {
    font-family: "Tinos", "Times New Roman", serif;
    font-size: 54px; color: var(--navy); line-height: 1.05; white-space: nowrap;
  }
  .identity-title {
    font-family: "Tinos", "Times New Roman", serif;
    font-size: 26px; color: var(--grey); margin-left: 40px;
  }
  .contact-box {
    position: absolute; border: 2px solid var(--navy); background: var(--paper);
    font-size: 20px; color: var(--ink); line-height: 1.35; white-space: nowrap;
  }
  .contact-phone { left: 70px; top: 220px; width: 220px; height: 86px; padding: 12px 0 0 34px; }
  .contact-web { left: 520px; top: 318px; width: 340px; height: 86px; padding: 12px 0 0 34px; }
  .contact-icon {
    position: absolute; left: -20px; top: 10px; width: 38px; height: 38px;
    border-radius: 50%; background: var(--navy);
  }
  .contact-icon svg { width: 38px; height: 38px; display: block; }
  .address {
    position: absolute; left: 60px; bottom: 42px;
    font-size: 22px; color: var(--paper); white-space: nowrap;
  }
  /* Back */
  .card-back {
    top: 630px;
    background: linear-gradient(135deg, var(--royal), var(--royal-light) 60%, var(--royal));
  }
  .back-rule {
    position: absolute; left: 0; top: 190px; width: 100%; height: 5px;
    background: var(--paper);
  }
  .back-frame {
    position: absolute; left: 215px; top: 130px; width: 470px; height: 125px;
    border: 2px solid var(--paper); background: var(--royal);
    display: flex; align-items: center; justify-content: center;
  }
  .back-wordmark { font-size: 50px; color: var(--paper); }
  .back-wordmark .wordmark-mark { background: var(--paper); }
</style>
</head>
<body>
  <section class="card card-front" aria-label="Business card front">
    <div class="front-pattern" role="img" aria-label="Faint grey block pattern background"></div>
    <div class="front-band"></div>

    <div class="wordmark front-wordmark">
      <span class="wordmark-mark"></span>ferngate build
    </div>

    <p class="registration">National Provider Number 7291<span class="sep"></span>ABN 53 219 864 317</p>

    <div class="identity">
      <p class="identity-name">Daniel Harper</p>
      <p class="identity-title">Chief Engineer</p>
    </div>

    <div class="contact-box contact-phone">
      <span class="contact-icon">
        <svg viewBox="0 0 38 38" aria-hidden="true">
          <path d="M11 15c0-3 4-5 8-5s8 2 8 5l-3 1-1-2h-8l-1 2z" fill="#fff"/>
          <rect x="12" y="18" width="14" height="9" rx="2" fill="#fff"/>
          <circle cx="19" cy="22.5" r="2.5" fill="#0b2a82"/>
        </svg>
      </span>
      0432 785 619<br>1300 987 214
    </div>

    <div class="contact-box contact-web">
      <span class="contact-icon">
        <svg viewBox="0 0 38 38" aria-hidden="true" fill="none" stroke="#fff" stroke-width="1.6">
          <circle cx="19" cy="19" r="10"/>
          <ellipse cx="19" cy="19" rx="4.5" ry="10"/>
          <path d="M9 19h20M11 13h16M11 25h16"/>
        </svg>
      </span>
      name@ferngatebuild.com.au<br>www.ferngatebuild.com.au
    </div>

    <p class="address">Level 3, 42 Marlow Street, Kotara NSW 2289</p>
  </section>

  <section class="card card-back" aria-label="Business card back">
    <div class="back-rule"></div>
    <div class="back-frame">
      <div class="wordmark back-wordmark">
        <span class="wordmark-mark"></span>ferngate build
      </div>
    </div>
  </section>
</body>
</html>
```